Medida Certa - Working hours register App needs interface design

Medida Certa, a 1 million users Brazilian website focused on general calculations needs an interface to an App for registering the working hours of a housemaid, a nanny, a housekeeper or other domestic workers.
The final users should be mainly housewifes.
The wireframe of the pages is in the LarPonto_layout.xls file attached.
Logo is also available in the wireframe.
The interface should be optimized for Android on Orbita KX with a 5'' screen.
Target Market(s)
Females, educated, from 30 to 50 y.o.
Industry/Entity Type
Android
Look and feel
Each slider illustrates characteristics of the customer's brand and the style your logo design should communicate.

```html
<!DOCTYPE html>
<html lang="en">
<head>
<meta charset="utf-8">
<title>Employee Registration</title>
<link rel="stylesheet" href="https://fonts.googleapis.com/css2?family=Barlow:wght@500;600;700&display=swap">
<style>
  :root {
    --brand-red: #c40000;
    --field-bg: #ebebeb;
    --accent-pink: #e8407a;
    --button-top: #ff5c8a;
    --button-bottom: #f23f72;
    --button-edge: #b8144a;
    --label-dark: #1c1c1c;
    --text-muted: #3c3c3c;
    --icon-grey: #5a5a5a;
    --white: #ffffff;
  }
  * { box-sizing: border-box; margin: 0; padding: 0; }
  html, body {
    width: 720px; height: 1200px; overflow: hidden;
    background: var(--white);
    font-family: "Barlow", "Arial Narrow", sans-serif;
  }
  .screen { position: relative; width: 720px; height: 1200px; }
  .app-header {
    height: 99px; background: var(--brand-red);
    display: flex; align-items: center; justify-content: center;
  }
  .app-title {
    color: var(--white); font-weight: 700; font-size: 51px; letter-spacing: 0.5px;
  }
  .form-field {
    position: absolute; left: 15px; width: 689px; height: 96px;
    background: var(--field-bg);
    border-bottom: 3px solid var(--accent-pink);
    display: flex; align-items: center; justify-content: space-between;
    padding: 0 24px 0 10px;
  }
  .field-label { font-size: 39px; font-weight: 600; color: var(--label-dark); }
  .edit-icon { width: 34px; height: 34px; fill: var(--icon-grey); }
  .save-button {
    position: absolute; left: 495px; top: 693px; width: 209px; height: 52px;
    background: linear-gradient(var(--button-top), var(--button-bottom));
    border-bottom: 3px solid var(--button-edge);
    display: flex; align-items: center; justify-content: center; gap: 12px;
    color: var(--white); font-weight: 700; font-size: 27px;
  }
  .save-button svg { width: 27px; height: 27px; fill: var(--white); }
  .schedule-list {
    position: absolute; left: 18px; top: 789px; width: 684px; list-style: none;
  }
  .schedule-row {
    height: 58.5px; display: flex; justify-content: space-between; align-items: center;
    font-size: 27px; font-weight: 600; color: var(--text-muted);
  }
  .app-footer {
    position: absolute; left: 0; bottom: 0; width: 720px; height: 24px;
    background: var(--brand-red);
  }
</style>
</head>
<body>
<div class="screen">
  <header class="app-header"><h1 class="app-title">Employee Registration</h1></header>

  <svg width="0" height="0" style="position:absolute">
    <symbol id="pencil" viewBox="0 0 24 24">
      <path d="M3 17.25V21h3.75L17.8 9.94l-3.75-3.75L3 17.25zM20.7 7.04a1 1 0 0 0 0-1.41l-2.34-2.34a1 1 0 0 0-1.41 0l-1.83 1.83 3.75 3.75 1.83-1.83z"/>
    </symbol>
  </svg>

  <div class="form-field" style="top:134px"><span class="field-label">Employer Name</span><svg class="edit-icon"><use href="#pencil"/></svg></div>
  <div class="form-field" style="top:273px"><span class="field-label">Nickname</span><svg class="edit-icon"><use href="#pencil"/></svg></div>
  <div class="form-field" style="top:414px"><span class="field-label">Date</span><svg class="edit-icon"><use href="#pencil"/></svg></div>
  <div class="form-field" style="top:564px"><span class="field-label">Social secure Number</span><svg class="edit-icon"><use href="#pencil"/></svg></div>

  <div class="save-button">
    <svg viewBox="0 0 24 24"><path d="M9 16.2 4.8 12l-2.1 2.1L9 20.4 22 7.4l-2.1-2.1z"/></svg>
    <span>Save</span>
  </div>

  <ul class="schedule-list">
    <li class="schedule-row"><span>Arrival</span><span>9:00</span></li>
    <li class="schedule-row"><span>Lunch Break Start</span><span>12:00</span></li>
    <li class="schedule-row"><span>Lunch Break End</span><span>12:30</span></li>
    <li class="schedule-row"><span>Out</span><span>17:30</span></li>
    <li class="schedule-row"><span>Saturday Work</span><span>Yes/No</span></li>
    <li class="schedule-row"><span>Has Lunch Break</span><span>Yes/No</span></li>
  </ul>

  <footer class="app-footer"></footer>
</div>
</body>
</html>
```